Community Bank Web Design

Design a homepage and internal product page for a community bank. Needs to be mobile friendly, minimal scrolling on home. Create the homepage look & feel, then use the same aesthetic to create the product page for the personal checking account page.

Wireframes, logo variations, and color scheme attached.

New brand identity:
• Open, Fresh, Younger, Bright, Bold, New, Innovative.
• Inviting, approachable, friendly, trustworthy.
• Imagine a young family purchasing their first home as the target audience.
You do not have to stick to the exact layout of the wireframes, as long as all of the elements are present.

All navigation elements are specified in wireframes. There are three versions of the homepage – Personal Home, Business Home, Wealth Management Home – you may design whichever version you prefer.

For internal page – please design the Checking product page, included in wireframes.

NOTE: Submit your homepage design first. I will provide feedback on your design direction, then you can use that to move forward with the internal page design.

Design direction--
Some banking / financial sites we like for their fresh/bold/open look:
velmorant.com
quendo.ca
rwxfinancial.org
pvt.co.nz
hopvault.com
pellerbank.com
ulk.co.nz

Target Market(s)

The target market for the personal homepage varies. Adults in the midwest, 25 - 60, who are striving to build their savings and manage their money. Often buying homes or refinancing their homes to make renovations, or planning for retirement.

For the business homepage, the target market are small to mid-market business owners striving to grow their business and manage their company.

Industry/Entity Type

Financial

Requirements
Must have
• colors: CRIMSON #a20c33,
FOREST GREEN #004f38
GOLD #e6a513

File format for design submission must be layered PSD (Please organize layers into recognizable folders like "menu" and "footer")

To make the design "mobile friendly" please create a grid-based layout. http://www.trovask.com/patterns/showPattern.php?patternID=grid-based-layout
http://www.quillbrightjournal.com/2007/04/14/designing-with-grid-based-approach/

```html
<!DOCTYPE html>
<html lang="en">
<head>
<meta charset="utf-8">
<title>Harrow Creek Bank – Personal Home</title>
<link rel="stylesheet" href="https://fonts.googleapis.com/css2?family=Hind:wght@400;500&family=Open+Sans:wght@400;600&display=swap">
<style>
:root{
  --crimson:#a20c33;
  --crimson-dark:#8c0a2b;
  --crimson-light:#b8123f;
  --gold:#eaa40e;
  --gold-dark:#d99608;
  --ink:#444;
  --muted:#8a8a8a;
  --panel:#e9e7e7;
  --line:#dedede;
  --soft:#f4f4f4;
  --white:#fff;
}
*{box-sizing:border-box;margin:0;padding:0}
html,body{width:1043px;height:1200px;overflow:hidden;background:var(--white)}
body{font-family:"Open Sans",Arial,sans-serif;color:var(--ink)}
.page{position:relative;width:1200px;height:1380px;transform:scale(.869167);transform-origin:0 0;border-top:5px solid var(--crimson)}
.abs{position:absolute}
a{color:inherit;text-decoration:none}
.head-font{font-family:"Hind",Arial,sans-serif}

/* header */
.brand{left:100px;top:22px;display:flex;align-items:center;gap:12px}
.brand-dot{width:58px;height:58px;border-radius:50%;background:var(--crimson)}
.brand-name{font-family:"Hind",sans-serif;font-weight:400;font-size:40px;color:var(--crimson);letter-spacing:-.5px}
.fdic{left:100px;top:92px;font-size:9px;color:#222;font-weight:600}
.utility{right:100px;top:18px;font-size:12px;color:#444}
.search{left:900px;top:58px;width:200px;height:38px;border:1px solid var(--line);border-radius:3px;font-size:13px;color:#999;padding:10px 10px}
.search svg{position:absolute;right:12px;top:12px}

/* nav */
.nav{left:100px;top:130px;width:1000px;height:61px;border-radius:3px;background:linear-gradient(var(--crimson-light),var(--crimson-dark));display:flex;font-family:"Hind",sans-serif;font-weight:500;font-size:16px;color:var(--white)}
.nav a{display:flex;align-items:center;justify-content:center;height:100%;border-right:1px solid rgba(0,0,0,.18);box-shadow:1px 0 0 rgba(255,255,255,.08)}
.nav a:last-child{border:none;box-shadow:none}
.nav svg{margin-right:5px}

/* login */
.login{left:100px;top:210px;width:257px;height:388px;background:var(--panel);border:1px solid #ddd}
.login-title{height:40px;border-bottom:1px solid #d6d4d4;font-family:"Hind",sans-serif;font-size:19px;padding:9px 20px;color:#444;background:#e3e1e1}
.field{position:absolute;left:15px;width:225px;height:42px;background:var(--white);border:1px solid #d8d8d8;border-radius:3px;font-size:13px;color:#555;padding:11px 20px}
.forgot{position:absolute;left:20px;top:187px;font-size:13px;color:var(--crimson);display:flex;align-items:center;gap:8px}
.tick{width:12px;height:12px;border-radius:50%;background:var(--white);border:1px solid #ccc}
.btn-login{position:absolute;left:15px;top:223px;width:224px;height:43px;border-radius:3px;background:linear-gradient(var(--crimson-light),var(--crimson-dark));color:var(--white);font-family:"Hind",sans-serif;font-size:15px;display:flex;align-items:center;justify-content:center;gap:4px}
.new-online{position:absolute;left:0;right:0;top:283px;text-align:center;font-family:"Hind",sans-serif;font-size:19px;color:#555}
.new-links{position:absolute;left:58px;top:314px;font-size:11px;color:var(--crimson);display:flex;gap:32px}
.apply{position:absolute;left:-1px;bottom:-1px;width:257px;height:47px;background:var(--gold);color:var(--white);font-family:"Hind",sans-serif;font-size:20px;text-align:center;padding-top:11px}

/* hero */
.hero{left:381px;top:210px;width:719px;height:389px;border:1px solid #e2e2e2}
.hero-photo{position:absolute;left:0;top:0;width:717px;height:340px;background:linear-gradient(100deg,#efe7de 0%,#d9c6b0 35%,#b9b3ad 60%,#8b7766 80%,#c8c0b5 100%)}
.arrow{position:absolute;top:157px;width:36px;height:36px;border-radius:50%;background:var(--white);border:2px solid #ccc;display:flex;align-items:center;justify-content:center}
.caption{position:absolute;left:0;top:340px;width:595px;height:47px;background:var(--soft);font-family:"Hind",sans-serif;font-size:18.5px;color:#555;padding:12px 28px}
.caption-btn{position:absolute;right:0;top:340px;width:123px;height:47px;background:var(--gold);color:var(--white);font-weight:600;font-size:14px;text-align:center;padding-top:14px}

/* feature */
.feature-photo{left:100px;top:634px;width:241px;height:228px;background:linear-gradient(#9bbf7a,#7fa55c 55%,#8c7a66 80%,#6e5b4b)}
.feature{left:366px;top:630px;width:437px}
.feature h2{font-family:"Hind",sans-serif;font-weight:400;font-size:19px;color:var(--crimson);margin-bottom:10px}
.feature p{font-size:12.8px;line-height:24px;text-align:justify;color:#555}
.btn{display:inline-block;background:var(--gold);color:var(--white);font-weight:600;font-size:14px;border-radius:2px;padding:9px 18px;border-bottom:2px solid var(--gold-dark)}
.feature .btn{margin-top:16px;margin-left:3px}
.rates{left:836px;top:633px;width:265px;height:230px;background:var(--soft);border:1px solid #e4e4e4;text-align:center;padding-top:18px}
.rates h2{font-family:"Hind",sans-serif;font-weight:400;font-size:31px;color:var(--crimson);margin-bottom:10px}
.rates p{font-size:12.8px;line-height:23px;color:var(--muted);padding:0 22px;margin-bottom:16px}

/* cards */
.card{top:909px;width:319px;height:317px;border:1px solid #e2e2e2;text-align:center;background:linear-gradient(#fff,#fbfbfb)}
.card-icon{height:60px;margin-top:34px;display:flex;align-items:center;justify-content:center}
.card h3{font-family:"Hind",sans-serif;font-weight:400;font-size:19.5px;color:#555;margin-top:42px}
.card p{font-size:13px;line-height:23px;color:var(--muted);padding:0 20px;margin-top:12px}
.card .btn{margin-top:14px}
.card-word{font-family:"Open Sans",sans-serif;font-weight:600;font-size:30px;color:#333}

/* footer */
.footer{left:0;top:1274px;width:1200px;height:106px;background:var(--crimson);color:var(--white)}
.footer-brand{position:absolute;left:100px;top:24px;display:flex;align-items:center;gap:10px}
.footer-dot{width:50px;height:50px;border-radius:50%;background:var(--white)}
.footer-name{font-family:"Hind",sans-serif;font-size:23px;line-height:24px}
.footer-legal{position:absolute;right:101px;top:27px;font-size:12.5px;text-align:right;line-height:30px}
.footer-code{position:absolute;right:36px;top:44px;font-size:12.5px}
</style>
</head>
<body>
<div class="page">

  <header>
    <div class="abs brand"><span class="brand-dot"></span><span class="brand-name">Harrow Creek Bank</span></div>
    <div class="abs fdic">Member FDIC</div>
    <div class="abs utility">Find a Branch or ATM &nbsp;\&nbsp; Contact Us</div>
    <div class="abs search">Search
      <svg width="14" height="14" viewBox="0 0 14 14"><circle cx="6" cy="6" r="4.5" fill="none" stroke="#aaa" stroke-width="1.6"/><line x1="9.3" y1="9.3" x2="13" y2="13" stroke="#aaa" stroke-width="1.8"/></svg>
    </div>
  </header>

  <nav class="abs nav">
    <a style="width:182px">Products &amp; Services</a>
    <a style="width:125px">Why HCB?</a>
    <a style="width:148px">Customer Center</a>
    <a style="width:110px">Personal</a>
    <a style="width:95px">Business</a>
    <a style="width:210px">Wealth Management</a>
    <a style="width:130px"><svg width="13" height="15" viewBox="0 0 13 15"><path d="M3 7V4.5a3.5 3.5 0 0 1 7 0V7" fill="none" stroke="#fff" stroke-width="2"/><rect x="0.5" y="7" width="12" height="8" rx="1" fill="#fff"/></svg>LOG IN</a>
  </nav>

  <section class="abs login">
    <div class="login-title">Account Type</div>
    <div class="field" style="top:60px">Banking</div>
    <div class="field" style="top:126px">User ID</div>
    <div class="forgot"><span class="tick"></span>Forgot User ID?</div>
    <div class="btn-login"><svg width="12" height="14" viewBox="0 0 13 15"><path d="M3 7V4.5a3.5 3.5 0 0 1 7 0V7" fill="none" stroke="#fff" stroke-width="2"/><rect x="0.5" y="7" width="12" height="8" rx="1" fill="#fff"/></svg>LOG IN</div>
    <div class="new-online">New to HCB Online?</div>
    <div class="new-links"><span>ENROLL</span><span>LEARN MORE</span></div>
    <div class="apply">Apply for a Loan</div>
  </section>

  <section class="abs hero">
    <div class="hero-photo" role="img" aria-label="Woman shopping online with a card at a laptop in a bright room with bookshelves"></div>
    <div class="arrow" style="left:21px"><svg width="10" height="14" viewBox="0 0 10 14"><path d="M8 1 2 7l6 6" fill="none" stroke="#333" stroke-width="2.6"/></svg></div>
    <div class="arrow" style="left:647px"><svg width="10" height="14" viewBox="0 0 10 14"><path d="m2 1 6 6-6 6" fill="none" stroke="#333" stroke-width="2.6"/></svg></div>
    <div class="caption">Rotating Promotional Messaging - ties to rotating large graphic</div>
    <a class="caption-btn">Learn More</a>
  </section>

  <div class="abs feature-photo" role="img" aria-label="Coin being dropped into a small model house on a green background"></div>
  <section class="abs feature">
    <h2>Home Equity Lines of Credit</h2>
    <p>Lorem ipsum dolor sit amet, consectetur adipiscing elit. Nulla quam velit, vulputate eu pharetra nec, mattis ac neque. Duis vulputate commodo lectus, ac blandit elit tincidunt id. Sed rhoncus, tortor sed eleifend tristique, tortor mauris molestie elit, et lacinia ipsum quam nec dui. Quisque nec mauris sit amet elit iaculis pretium sit amet quis magna. Aenean velit odio, elementum in tempus ut, vehicula eu diam.</p>
    <a class="btn">Learn More</a>
  </section>

  <aside class="abs rates">
    <h2>Rates</h2>
    <p>Rates vary daily - sometimes by the hour. Find out what you need to know. Rates vary daily - sometimes by the hour.</p>
    <a class="btn">View Rates</a>
  </aside>

  <article class="abs card" style="left:100px">
    <div class="card-icon"><svg width="42" height="64" viewBox="0 0 42 64"><rect x="1" y="1" width="40" height="62" rx="6" fill="#333"/><rect x="5" y="9" width="32" height="42" fill="#fff"/><circle cx="21" cy="57" r="3" fill="#fff"/></svg></div>
    <h3>Mobile Deposit. It's easy!</h3>
    <p>Lorem ipsum dolor sit amet, consectetur adipiscing elit. Nulla quam velit, vulputate eu pharetra nec, mattis ac neque.</p>
    <a class="btn">Learn More</a>
  </article>

  <article class="abs card" style="left:440px">
    <div class="card-icon"><svg width="56" height="54" viewBox="0 0 56 54"><path d="M28 2 2 27l4 4 4-4v25h14V38h8v14h14V27l4 4 4-4L40 13V5h-6v3z" fill="#333"/></svg></div>
    <h3>Looking for a New Home?</h3>
    <p>Lorem ipsum dolor sit amet, consectetur adipiscing elit. Nulla quam velit, vulputate eu pharetra nec, mattis ac neque.</p>
    <a class="btn">Find your Mortgage Banker</a>
  </article>

  <article class="abs card" style="left:780px">
    <div class="card-icon"><span class="card-word">Corvia</span></div>
    <h3>Corvia Debit Cards</h3>
    <p>Lorem ipsum dolor sit amet, consectetur adipiscing elit. Nulla quam velit, vulputate eu pharetra nec, mattis ac neque.</p>
    <a class="btn">Learn More</a>
  </article>

  <footer class="abs footer">
    <div class="footer-brand"><span class="footer-dot"></span><span class="footer-name">Harrow Creek<br>Bank</span></div>
    <div class="footer-legal">2014 Harrow Creek Bank of Larkton. Equal Housing Lender and Member FDIC.<br>Privacy Policy &nbsp;| &nbsp;Security &nbsp;| &nbsp;CRA &nbsp;| &nbsp;Other required information</div>
    <div class="footer-code">X18</div>
  </footer>

</div>
</body>
</html>
```